The most modern business card ever !!!

Our company call “Vantilo”. Vantilo is a technology company specialized in cruises solutions. Out main product is a platform to reserve cruises. This is a revolutionary platform that make easier to travel agencies and final users to reserve cruises across dozen companies like tarvik, welbi, dpv, hbt, etc..We are a “start up”, with a young team of developers and we want to transmit it.. For it, we want something different, a modern business card that represent cruises and technology.. When someone receive this card, this person should say: wowww this is different… this is modern… this is a cruise related company..
Contact Information for Business Card
Requirements
Must have
- diferent, modern
Should not have
- traditions business card

```html
<!DOCTYPE html>
<html lang="en">
<head>
<meta charset="UTF-8">
<title>Vantilo — Business Card</title>
<link href="https://fonts.googleapis.com/css2?family=Montserrat:wght@400;500;600&display=swap" rel="stylesheet">
<style>
  :root {
    --backdrop: #2a2a2c;
    --card-dark: #1f1d21;
    --clear-top: #a7a9ac;
    --clear-bottom: #86898c;
    --accent: #2fa8dc;
    --text-light: #f2f2f2;
  }
  * { margin: 0; padding: 0; box-sizing: border-box; }
  html, body {
    width: 1200px; height: 900px; overflow: hidden;
    background: var(--backdrop);
    font-family: "Montserrat", sans-serif;
  }
  .canvas {
    width: 1200px; height: 900px;
    display: flex; align-items: center; justify-content: center;
  }
  .business-card {
    position: relative;
    width: 900px; height: 515px;
    border-radius: 26px;
    overflow: hidden;
    background: linear-gradient(160deg, var(--clear-top), var(--clear-bottom));
    box-shadow: 0 18px 40px rgba(0,0,0,0.45);
  }
  .accent-band {
    position: absolute; inset: 0;
    width: 900px; height: 515px;
  }
  .info-panel {
    position: absolute; left: 0; top: 0;
    width: 520px; height: 100%;
    background: var(--card-dark);
    padding: 62px 0 0 62px;
    color: var(--text-light);
  }
  .person-name {
    font-size: 25px; font-weight: 500;
    letter-spacing: 0.5px; text-transform: uppercase;
  }
  .person-role {
    margin-top: 4px;
    font-size: 15px; font-weight: 500;
    color: var(--accent);
    letter-spacing: 0.8px; text-transform: uppercase;
  }
  .contact-list { list-style: none; margin-top: 34px; }
  .contact-item {
    display: flex; align-items: flex-start; gap: 16px;
    font-size: 16px; line-height: 1.3;
    text-transform: uppercase; letter-spacing: 0.3px;
    margin-bottom: 24px;
  }
  .contact-icon { flex: none; width: 24px; height: 24px; }
  .brand-name {
    position: absolute; left: 62px; bottom: 56px;
    font-size: 62px; font-weight: 400;
    color: var(--text-light);
    letter-spacing: 1px;
  }
</style>
</head>
<body>
<main class="canvas">
  <article class="business-card">
    <svg class="accent-band" viewBox="0 0 900 515" aria-hidden="true">
      <polygon points="860,0 900,0 900,40 610,515 540,515" fill="var(--accent)"/>
    </svg>

    <section class="info-panel">
      <h1 class="person-name">Marek Holloway</h1>
      <p class="person-role">Managing Director</p>

      <ul class="contact-list">
        <li class="contact-item">
          <svg class="contact-icon" viewBox="0 0 24 24" aria-hidden="true">
            <circle cx="12" cy="12" r="12" fill="var(--accent)"/>
            <path d="M8.5 6.5l2 2-1.2 1.6c.7 1.6 1.9 2.8 3.5 3.5l1.6-1.2 2 2-1.3 1.8c-3.9-.3-7.2-3.6-7.5-7.5z" fill="#fff"/>
          </svg>
          <span>555 210 48 73</span>
        </li>
        <li class="contact-item">
          <svg class="contact-icon" viewBox="0 0 24 24" aria-hidden="true">
            <circle cx="12" cy="12" r="12" fill="var(--accent)"/>
            <path d="M12 5.5a4 4 0 0 0-4 4c0 3 4 8 4 8s4-5 4-8a4 4 0 0 0-4-4zm0 5.5a1.5 1.5 0 1 1 0-3 1.5 1.5 0 0 1 0 3z" fill="#fff"/>
          </svg>
          <span>48 Harbor Lane<br>Bayview, New York 10482</span>
        </li>
        <li class="contact-item">
          <svg class="contact-icon" viewBox="0 0 24 24" aria-hidden="true">
            <circle cx="12" cy="12" r="12" fill="var(--accent)"/>
            <rect x="6.5" y="8" width="11" height="8" rx="1" fill="#fff"/>
            <path d="M6.8 8.5l5.2 4 5.2-4" fill="none" stroke="var(--accent)" stroke-width="1.2"/>
          </svg>
          <span>m.holloway@vantilo.com<br>www.vantilo.com</span>
        </li>
      </ul>

      <p class="brand-name">Vantilo</p>
    </section>
  </article>
</main>
</body>
</html>
```